Tidewell Ventures Wordpress / Web Design - Agile Coaching

UPDATE: PLEASE USE MORE ICONS/GRAPHICS THEN PHOTOS. THANK YOU!

We need a web design for a new company called Tidewell Ventures. We do agile coaching, consulting, training and facilitation for medium to large enterprise, most just starting their agile journey. We want to be professional, but light and whimsical. We have started loading content onto the www.tidewellventures.example website, using the Marlow Theme (real flexibility!)

We have a logo, and I really liked it, although if needed the colors can be adjusted depending on the design. I would advice sticking with the logo and its colors unless they become problematic or you have a fantastic idea.

I really like the colors found on stickum slips, and use stickum slips in all my coaching and training. I want to warn though, I don't want the whole site to be splashes of color, but I would like some pop of color, and you could use the stickum slip colors and the idea of stickum slips for icon designs or sparingly for emphasis, but keep the design simple with lots of white space. I'm inspired by this template from Pattern Bazaar and use the power point in the 2nd attached file...this may inspire you.

I have another contest running right now, if you want to check that out as well, but it isn't necessary. Contest is titled "Tidewell Ventures: Software Development Consultancy Needs a Business Card Design"

Target Market(s)

medium to large software companies needing to improve the speed, quality and value of their software delivery

Industry/Entity Type

Information Technology

Number of Pages Required

3 page

Font styles to use
Sans Serif

Requirements
Must have
• Simple, easy to use, easy navigation, space!
• content on my front page is accurate so should be included www.tidewellventures.example
• 2nd page you can look at is http://www.tidewellventures.example/inspiration/
• 3rd page you can look at is http://www.tidewellventures.example/reference-list/ (about twice as many links are going to be added in next two days!)
Nice to have
• take a look at any other page on the site. if something is password protected, use the word "password" as the password.
• Update: I like less pictures, more graphics.
Should not have
• too crowded. hard to navigate. childish graphics. too boring and corporate. :)

```html
<!DOCTYPE html>
<html lang="en">
<head>
<meta charset="utf-8">
<title>Tidewell Ventures – Agile Coaching</title>
<link rel="stylesheet" href="https://fonts.googleapis.com/css2?family=Open+Sans:wght@400;600;700&display=swap">
<style>
:root{
  --navy:#1c2c4c;
  --ink:#333a44;
  --muted:#7b838d;
  --line:#e4e6e9;
  --teal:#4a9ea6;
  --red:#e2503f;
  --purple:#8b3f8f;
  --green:#2fa84f;
  --blue:#2d92d2;
  --footer:#2c3037;
  --footer-deep:#202328;
  --white:#ffffff;
}
*{box-sizing:border-box;margin:0;padding:0}
html,body{width:721px;height:1200px;overflow:hidden;background:var(--white)}
body{font-family:"Open Sans",Arial,sans-serif;color:var(--ink);position:relative}
.topbar{position:absolute;left:0;top:0;width:721px;height:17px;background:var(--navy);color:#c9d2e3;font-size:7px;display:flex;align-items:center;justify-content:space-between;padding:0 58px}
.topbar span{margin-right:12px}
.header{position:absolute;top:17px;left:0;width:721px;height:67px;display:flex;align-items:center;justify-content:space-between;padding:0 58px;border-bottom:1px solid var(--line)}
.brand{display:flex;align-items:center;gap:7px;font-weight:700;font-size:15px;color:var(--navy)}
.brand-dot{width:22px;height:22px;border-radius:50%;background:var(--blue)}
.nav{display:flex;gap:26px;font-size:9px;color:var(--ink)}
.nav .active{color:var(--blue)}
.hero{position:absolute;top:84px;left:0;width:721px;height:341px;background:linear-gradient(100deg,#1b1f24 0%,#2e3339 50%,#6c747b 72%,#2a2e33 100%)}
.hero-copy{position:absolute;left:68px;top:78px;width:250px;color:var(--white)}
.hero-copy h1{font-size:24px;font-weight:700;margin-bottom:12px}
.hero-copy p{font-size:10px;line-height:1.6;margin-bottom:22px}
.btn{display:inline-block;background:var(--teal);color:var(--white);font-size:8px;padding:7px 14px;border-radius:2px}
.hero-arrow{position:absolute;top:160px;width:18px;height:22px}
.welcome{position:absolute;top:436px;left:0;width:721px;text-align:center}
.welcome h2{font-size:17px;font-weight:600;color:var(--ink)}
.welcome .sub{font-size:8px;color:var(--muted);margin-top:8px}
.services{position:absolute;top:493px;left:58px;width:605px;display:flex;justify-content:space-between}
.service{width:136px;text-align:center}
.service .icon{width:58px;height:58px;border-radius:50%;margin:0 auto 14px;display:flex;align-items:center;justify-content:center}
.service h3{font-size:10px;font-weight:700;margin-bottom:8px}
.service p{font-size:7px;color:var(--muted);line-height:1.55;margin-bottom:12px}
.service .btn{font-size:7px;padding:5px 12px}
.about{position:absolute;top:688px;left:58px;width:605px;display:flex;gap:26px}
.about-photo{width:180px;height:96px;background:linear-gradient(160deg,#dfe8f1 0%,#8ea4bb 50%,#4c5b6c 100%)}
.about-copy h2{font-size:14px;font-weight:600;margin-bottom:6px}
.about-copy p{font-size:7px;color:var(--muted);line-height:1.6;margin-bottom:8px}
.about-copy .btn{font-size:7px;padding:5px 12px}
.posts-head{position:absolute;top:800px;left:58px;width:605px}
.posts-head h2{font-size:14px;font-weight:600}
.posts-head p{font-size:7px;color:var(--muted);margin-top:5px}
.posts-head .btn{position:absolute;right:0;top:0;font-size:7px;padding:6px 12px}
.posts{position:absolute;top:846px;left:58px;width:605px;display:flex;justify-content:space-between}
.post{width:143px}
.post-thumb{height:94px;margin-bottom:8px}
.post h4{font-size:8px;font-weight:700}
.post time{display:block;font-size:6px;color:var(--muted);margin-top:3px}
.footer{position:absolute;top:972px;left:0;width:721px;height:204px;background:var(--footer);color:#b8bdc4;padding:22px 58px;display:flex;gap:28px}
.footer h5{font-size:7px;font-weight:700;color:var(--white);letter-spacing:.5px;margin-bottom:10px;text-transform:uppercase}
.col-quote{width:150px}
.quote{background:#383d45;padding:9px;font-size:7px;line-height:1.55;font-style:normal}
.author{display:flex;align-items:center;gap:7px;margin-top:10px;font-size:7px}
.avatar{width:24px;height:24px;border-radius:50%;background:#8a9099}
.author strong{color:var(--white);display:block}
.col-links{width:90px;font-size:7px;line-height:2}
.col-contact{width:120px;font-size:7px;line-height:2}
.footer-brand{margin-left:auto;margin-top:36px;display:flex;align-items:center;gap:9px;font-size:17px;font-weight:700;color:#9aa0a8}
.footer-brand .brand-dot{width:34px;height:34px;background:#5b6069}
.copyright{position:absolute;top:1176px;left:0;width:721px;height:24px;background:var(--footer-deep);color:#7c828a;font-size:6px;display:flex;align-items:center;justify-content:center}
</style>
</head>
<body>
<div class="topbar">
  <div><span>Call us: +1 (555) 014-2290</span><span>Email: hello@tidewellventures.example</span></div>
  <div>Connect with our social network</div>
</div>

<header class="header">
  <div class="brand"><span class="brand-dot"></span>Tidewell Ventures</div>
  <nav class="nav">
    <span class="active">Home</span><span>Services</span><span>Inspiration</span><span>Availability</span><span>Blog</span><span>Contact</span>
  </nav>
</header>

<section class="hero" role="img" aria-label="Hands holding a glowing clock face against a dark background">
  <svg class="hero-arrow" style="left:8px" viewBox="0 0 18 22"><path d="M12 4 5 11l7 7" fill="none" stroke="#fff" stroke-width="2"/></svg>
  <svg class="hero-arrow" style="right:8px" viewBox="0 0 18 22"><path d="M6 4l7 7-7 7" fill="none" stroke="#fff" stroke-width="2"/></svg>
  <div class="hero-copy">
    <h1>We do agile coaching</h1>
    <p>We do agile coaching, consulting, training and facilitation for medium to large enterprise, most just starting their agile journey.</p>
    <span class="btn">Read more info</span>
  </div>
</section>

<section class="welcome">
  <h2>Welcome to Tidewell Ventures</h2>
  <p class="sub">We do agile coaching, consulting, training and facilitation for medium to large enterprise, most just starting their agile journey.</p>
</section>

<section class="services">
  <article class="service">
    <div class="icon" style="background:var(--red)"><svg width="28" height="28" viewBox="0 0 28 28"><circle cx="10" cy="9" r="4" fill="#fff"/><circle cx="19" cy="10" r="3" fill="#fff"/><path d="M3 23c0-5 3-8 7-8s7 3 7 8zM15 23c0-4 2-7 5-7s5 3 5 7z" fill="#fff"/></svg></div>
    <h3>Coaching</h3>
    <p>What is the next step? Let's figure that out. We guide teams as they learn to plan, build and deliver value sooner.</p>
    <span class="btn">Read more</span>
  </article>
  <article class="service">
    <div class="icon" style="background:var(--purple)"><svg width="28" height="28" viewBox="0 0 28 28"><path d="M4 6h20v12H12l-5 4v-4H4z" fill="#fff"/></svg></div>
    <h3>Consulting</h3>
    <p>What is the next step? Let's figure that out. We review how you work and map a clear path to better delivery.</p>
    <span class="btn">Read more</span>
  </article>
  <article class="service">
    <div class="icon" style="background:var(--green)"><svg width="28" height="28" viewBox="0 0 28 28"><path d="M3 8l11-4 11 4-11 4z" fill="#fff"/><path d="M8 11v6c0 2 3 3 6 3s6-1 6-3v-6l-6 2z" fill="#fff"/></svg></div>
    <h3>Training</h3>
    <p>What is the next step? Let's figure that out. Hands-on classes give teams the shared language of agile work.</p>
    <span class="btn">Read more</span>
  </article>
  <article class="service">
    <div class="icon" style="background:var(--blue)"><svg width="28" height="28" viewBox="0 0 28 28"><path d="M5 10h14l-4-4M23 18H9l4 4" fill="none" stroke="#fff" stroke-width="2.4" stroke-linecap="round" stroke-linejoin="round"/></svg></div>
    <h3>Facilitation</h3>
    <p>What is the next step? Let's figure that out. We run focused sessions so every voice is heard and decisions stick.</p>
    <span class="btn">Read more</span>
  </article>
</section>

<section class="about">
  <div class="about-photo" role="img" aria-label="Glass office towers seen from below against a pale sky"></div>
  <div class="about-copy">
    <h2>About Tidewell Ventures</h2>
    <p>Our small team has spent years helping software groups move from long release cycles to steady, predictable delivery. We start with where you are, listen closely, and build simple habits that last. Coaching, training and facilitation work together so that change feels natural rather than forced, and every team can see progress week by week.</p>
    <span class="btn">Read more info</span>
  </div>
</section>

<section class="posts-head">
  <h2>Recent Posts</h2>
  <p>We do agile coaching, consulting, training and facilitation for medium to large enterprise, most just starting their agile journey.</p>
  <span class="btn">View more posts</span>
</section>

<section class="posts">
  <article class="post">
    <div class="post-thumb" role="img" aria-label="Hand touching a glowing green digital interface" style="background:linear-gradient(135deg,#0f2a1e,#2f6b4a 60%,#9fd3a8)"></div>
    <h4>How do you like your lasagna?</h4><time>Posted on 21 March 2014</time>
  </article>
  <article class="post">
    <div class="post-thumb" role="img" aria-label="Businessman leaping between cliffs under a blue sky" style="background:linear-gradient(180deg,#a9cdea,#e8f1f8 65%,#7b8794)"></div>
    <h4>How do you like your lasagna?</h4><time>Posted on 21 March 2014</time>
  </article>
  <article class="post">
    <div class="post-thumb" role="img" aria-label="Close-up of a compass on a blue background" style="background:radial-gradient(circle at 50% 50%,#dfe6ee,#4d78a8 55%,#1e3a63)"></div>
    <h4>How do you like your lasagna?</h4><time>Posted on 21 March 2014</time>
  </article>
  <article class="post">
    <div class="post-thumb" role="img" aria-label="Row of dark fruit with one bright one standing out" style="background:linear-gradient(90deg,#111,#3a3a3a 55%,#6b6b6b)"></div>
    <h4>How do you like your lasagna?</h4><time>Posted on 21 March 2014</time>
  </article>
</section>

<footer class="footer">
  <div class="col-quote">
    <h5>Testimonials</h5>
    <blockquote class="quote">Working with this team changed how we plan. Releases are calmer, meetings are shorter and people enjoy the work again.</blockquote>
    <div class="author"><span class="avatar" role="img" aria-label="Client portrait placeholder"></span><div><strong>Jordan Ellis</strong>Delivery Manager</div></div>
  </div>
  <div class="col-links">
    <h5>Welcome</h5>
    <div>Home</div><div>Services</div><div>Inspiration</div><div>Availability</div><div>Blog</div><div>Contact</div>
  </div>
  <div class="col-contact">
    <h5>Contact</h5>
    <div>48 Harbor Lane</div><div>Fairview, VA 20100</div><div>+1 (555) 014-2290</div><div>hello@tidewellventures.example</div>
  </div>
  <div class="footer-brand"><span class="brand-dot"></span>Tidewell Ventures</div>
</footer>
<div class="copyright">© 2014 Tidewell Ventures. All rights reserved.</div>
</body>
</html>
```